Colton's Heating needs SUV Wrap design

We are looking for options for an SUV wrap, we currently have a van wrap which we would like to play off to design the SUV wrap. We would like to see designs that use our logo as well as our van wrap to stay branded.

Colors; Navy blue & grey as in logo
Design - Minimal design - not full truck. 1/2 of back - no design on front end
Please see our current warps to match style.

I have attached full ZIP file of logo

Industry/Entity Type

HVAC

Font styles to use
Serif
Sans Serif

Colors
0054AA
0677BA
7BADD7
CADEEF
E8F1F8

Requirements
Must have
• Minimalist wrap design - Must have name of company and logo. Colors: Blue and Navy
Should not have
• Full wrap, other colors and fonts that don't match our current design

```html
<!DOCTYPE html>
<html lang="en">
<head>
<meta charset="utf-8">
<title>Colton's Heating – SUV Wrap</title>
<link href="https://fonts.googleapis.com/css2?family=Arimo:wght@400;700&display=swap" rel="stylesheet">
<style>
  :root{
    --navy:#0a3a96;
    --grey:#8e8e90;
    --grey-dark:#6f6f72;
    --body:#e9e9ea;
    --body-shade:#d2d2d4;
    --glass:#2a2d33;
    --tyre:#1d1d1f;
    --rim:#b9bbbe;
    --light:#f3f3f3;
    --bg:#f4f5f7;
  }
  html,body{margin:0;padding:0;overflow:hidden;background:var(--bg);}
  .canvas{width:1200px;height:667px;display:block;}
  .brand-name{font-family:"Arimo",sans-serif;font-weight:700;fill:var(--navy);font-size:34px;}
  .tagline{font-family:"Arimo",sans-serif;font-weight:700;fill:var(--navy);font-size:9.5px;}
  .phone{font-family:"Arimo",sans-serif;font-weight:700;fill:var(--light);font-size:20px;}
  .services{font-family:"Arimo",sans-serif;font-weight:700;fill:#dcdcdc;font-size:8.5px;}
  .website{font-family:"Arimo",sans-serif;font-weight:700;fill:var(--navy);font-size:10px;}
  .badge-text{font-family:"Arimo",sans-serif;font-weight:700;fill:var(--navy);font-size:6.5px;}
</style>
</head>
<body>
<svg class="canvas" viewBox="0 0 1200 667" xmlns="http://www.w3.org/2000/svg">
  <defs>
    <clipPath id="body-clip">
      <path d="M252 272 L250 215 L258 150 L275 110 L305 58 L640 44 L790 125 L955 158 L995 195 L1000 262 L985 278 L940 278 A62 62 0 0 0 808 278 L462 278 A62 62 0 0 0 338 278 Z"/>
    </clipPath>
    <g id="suv">
      <path class="suv-body" fill="var(--body)" stroke="#bdbdc0" stroke-width="1"
        d="M252 272 L250 215 L258 150 L275 110 L305 58 L640 44 L790 125 L955 158 L995 195 L1000 262 L985 278 L940 278 A62 62 0 0 0 808 278 L462 278 A62 62 0 0 0 338 278 Z"/>
      <g clip-path="url(#body-clip)">
        <path class="wrap-grey" fill="var(--grey)" d="M250 110 L640 95 L800 190 L800 200 L640 280 L250 280 Z"/>
        <path class="wrap-grey-dark" fill="var(--grey-dark)" d="M250 110 L420 100 L470 280 L250 280 Z" opacity=".55"/>
        <path class="wrap-light-slash" fill="#b3b3b5" d="M520 180 L800 196 L800 250 L600 280 L500 280 Z" opacity=".7"/>
        <path class="wrap-stripe" fill="var(--navy)" d="M250 160 L345 160 L335 200 L250 198 Z"/>
        <path class="wrap-stripe" fill="var(--navy)" d="M250 200 L335 205 L345 240 L250 236 Z"/>
        <path class="wrap-stripe" fill="var(--navy)" d="M470 252 L620 262 L470 262 Z"/>
        <path class="wrap-stripe" fill="var(--navy)" d="M575 118 L645 142 L645 147 L575 124 Z"/>
        <path class="wrap-stripe" fill="var(--navy)" d="M275 108 L330 48 L470 46 L300 60 Z"/>
        <rect x="250" y="262" width="760" height="20" fill="var(--body-shade)"/>
      </g>
      <path class="rear-glass" fill="var(--navy)" d="M285 108 L318 60 L445 56 L430 100 Z"/>
      <path class="side-glass" fill="var(--glass)" d="M475 98 L495 58 L610 56 L608 96 Z"/>
      <path class="side-glass" fill="var(--glass)" d="M622 96 L624 56 L650 56 L745 122 L622 112 Z"/>
      <line x1="615" y1="55" x2="615" y2="260" stroke="#a9a9ac" stroke-width="1.2"/>
      <line x1="470" y1="100" x2="470" y2="255" stroke="#a9a9ac" stroke-width="1"/>
      <path fill="#9c1f26" d="M253 132 L300 128 L296 145 L255 148 Z"/>
      <path fill="#cfd3d8" d="M955 160 L990 165 L992 175 L958 172 Z"/>
      <path fill="#dcdcdd" d="M745 108 L770 110 L772 128 L748 126 Z"/>
      <g class="wheel">
        <circle cx="400" cy="283" r="55" fill="var(--tyre)"/>
        <circle cx="400" cy="283" r="40" fill="var(--rim)"/>
        <circle cx="400" cy="283" r="8" fill="#8b8d90"/>
      </g>
      <g class="wheel">
        <circle cx="874" cy="283" r="55" fill="var(--tyre)"/>
        <circle cx="874" cy="283" r="40" fill="var(--rim)"/>
        <circle cx="874" cy="283" r="8" fill="#8b8d90"/>
      </g>
    </g>
  </defs>

  <!-- driver side view (facing right) -->
  <g class="suv-view suv-view--right">
    <use href="#suv"/>
    <g class="service-badge">
      <circle cx="338" cy="148" r="12" fill="none" stroke="var(--navy)" stroke-width="2.5"/>
      <text class="badge-text" x="355" y="152" transform="rotate(12 355 152)">SERVICE</text>
      <text class="badge-text" x="356" y="161" transform="rotate(12 356 161)">AVALIABLE</text>
    </g>
    <g class="brand-lockup">
      <circle cx="430" cy="150" r="20" fill="none" stroke="var(--navy)" stroke-width="4"/>
      <text class="brand-name" x="460" y="160" transform="rotate(12 460 160)">Colton's</text>
      <text class="brand-name" x="478" y="194" transform="rotate(12 478 194)">Heating</text>
    </g>
    <text class="website" x="462" y="232" transform="rotate(12 462 232)">www.ColtonsHeating.com</text>
    <text class="tagline" x="675" y="158" transform="rotate(12 675 158)">Commercial &amp; Residential</text>
    <text class="phone" x="668" y="182" transform="rotate(12 668 182)">555.014.2760</text>
    <g class="services" transform="rotate(12 680 207)">
      <text x="680" y="207">• Preventative Maintenance</text>
      <text x="678" y="219">• Sheet Metal Fabrication</text>
      <text x="676" y="231">• Indoor Air Quality</text>
      <text x="674" y="243">• Installation</text>
      <text x="672" y="255">• Service</text>
    </g>
  </g>

  <!-- passenger side view (facing left) -->
  <g class="suv-view suv-view--left">
    <use href="#suv" transform="translate(1200 333) scale(-1 1)"/>
    <g class="service-badge">
      <circle cx="862" cy="481" r="12" fill="none" stroke="var(--navy)" stroke-width="2.5"/>
      <text class="badge-text" x="845" y="485" text-anchor="end" transform="rotate(-12 845 485)">SERVICE</text>
      <text class="badge-text" x="844" y="494" text-anchor="end" transform="rotate(-12 844 494)">AVALIABLE</text>
    </g>
    <g class="brand-lockup" text-anchor="end">
      <circle cx="770" cy="483" r="20" fill="none" stroke="var(--navy)" stroke-width="4"/>
      <text class="brand-name" x="740" y="493" transform="rotate(-12 740 493)">Colton's</text>
      <text class="brand-name" x="722" y="527" transform="rotate(-12 722 527)">Heating</text>
    </g>
    <text class="website" x="738" y="565" text-anchor="end" transform="rotate(-12 738 565)">www.ColtonsHeating.com</text>
    <text class="tagline" x="525" y="491" text-anchor="end" transform="rotate(-12 525 491)">Commercial &amp; Residential</text>
    <text class="phone" x="532" y="515" text-anchor="end" transform="rotate(-12 532 515)">555.014.2760</text>
    <g class="services" text-anchor="end" transform="rotate(-12 520 540)">
      <text x="520" y="540">Preventative Maintenance •</text>
      <text x="522" y="552">Sheet Metal Fabrication •</text>
      <text x="524" y="564">Indoor Air Quality •</text>
      <text x="526" y="576">Installation •</text>
      <text x="528" y="588">Service •</text>
    </g>
  </g>
</svg>
</body>
</html>
```